Willowmere Handmade needs packaging for Bars of Soap

I need a design for packaging bars of soap. My soaps are focused on quality ingredients, utilising Australian Clay's and unique Australian essential oils. The Soaps are designed to benefit the skin by lightly exfoliating, cleansing while moisturizing and softening the skin.

I am wanting a soap box designed.
The box should be 95mm x 70mm x 28mm
Have an upmarket quality feel.
I am thinking of using grey, but am open to other natural colours.
The box will have the logo, web address, space left so I can add the ingredient list.
The text 'Handcrafted in Bellhaven' on the box. (If it fits comfortably)

Target Market(s)

25-50yrs , health and body conscious

Industry/Entity Type

Health And Wellness

Requirements
Must have
• include the web address.
• space for the scent/type of clay for each soap. This will change, as will the ingredients as I create new soaps. I would like the ability to change this as required easily myself if possible?
Nice to have
• I am swaying towards grey but am not locked in to it.
• Handcrafted in Bellhaven (text added on the box)

```html
<!DOCTYPE html>
<html lang="en">
<head>
<meta charset="utf-8">
<title>Willowmere Handmade – Soap Box Fronts</title>
<link rel="stylesheet" href="https://fonts.googleapis.com/css2?family=Amatic+SC:wght@700&family=Arimo:wght@400&display=swap">
<style>
  :root {
    --bg: #f4f4f4;
    --paper: #e6e6e6;
    --paper-light: #f0f0f0;
    --citrus: #3f7d34;
    --lavender: #625f4e;
    --ink-body: #4a4a4a;
    --white: #ffffff;
  }
  * { box-sizing: border-box; margin: 0; padding: 0; }
  html, body {
    width: 1200px; height: 1200px; overflow: hidden;
    background: var(--bg);
  }
  .stage {
    position: relative; width: 1200px; height: 1200px;
    display: flex; justify-content: center; align-items: center; gap: 80px;
  }
  .box-front {
    --accent: var(--citrus);
    position: relative; width: 440px; height: 640px;
    background: linear-gradient(180deg, var(--paper-light), var(--paper));
    box-shadow: 0 18px 40px rgba(0,0,0,0.12);
    overflow: hidden;
  }
  .box-front.lavender { --accent: var(--lavender); }
  .top-band {
    position: absolute; left: 0; top: 0; width: 100%; height: 34px;
    background: var(--accent);
  }
  .brand-name {
    position: absolute; left: 0; right: 0; top: 150px; text-align: center;
    font-family: "Arimo", sans-serif; font-weight: 400;
    font-size: 34px; line-height: 1.2; color: var(--accent);
  }
  .description {
    position: absolute; left: 112px; top: 250px; width: 228px;
    font-family: "Arimo", sans-serif; font-size: 13px; line-height: 1.38;
    color: var(--ink-body); text-align: justify;
  }
  .scent-tab {
    position: absolute; right: 0; top: 390px; width: 200px; height: 66px;
    background: var(--accent); border: 3px solid var(--paper-light); border-right: 0;
    display: flex; align-items: center; justify-content: center;
    font-family: "Amatic SC", cursive; font-weight: 700; font-size: 32px;
    letter-spacing: 0.22em; color: var(--white);
  }
  .band-rule {
    position: absolute; left: 0; top: 428px; width: 240px; height: 3px;
    background: var(--accent);
  }
  .pattern-band {
    position: absolute; left: 0; top: 440px; width: 100%; height: 146px;
    background: var(--accent);
  }
  .origin {
    position: absolute; left: 0; right: 0; bottom: 18px; text-align: center;
    font-family: "Arimo", sans-serif; font-size: 21px; color: var(--accent);
  }
</style>
</head>
<body>
<main class="stage">
  <section class="box-front citrus">
    <div class="top-band"></div>
    <h1 class="brand-name">Willowmere Handmade</h1>
    <p class="description">Soaps are focused on quality ingredients, utilising Australian Clay's and unique Australian essential oils. The Soaps are designed to benefit the skin by lightly exfoliating, cleansing while moisturizing and softening the skin.</p>
    <div class="band-rule"></div>
    <div class="pattern-band" role="img" aria-label="Band of white hand-drawn spiral swirls on green"></div>
    <div class="scent-tab">Fresh Citrus</div>
    <p class="origin">Handcrafted in Bellhaven</p>
  </section>

  <section class="box-front lavender">
    <div class="top-band"></div>
    <h1 class="brand-name">Willowmere Handmade</h1>
    <p class="description">Soaps are focused on quality ingredients, utilising Australian Clay's and unique Australian essential oils. The Soaps are designed to benefit the skin by lightly exfoliating, cleansing while moisturizing and softening the skin.</p>
    <div class="band-rule"></div>
    <div class="pattern-band" role="img" aria-label="Band of white hand-drawn spiral swirls on olive grey"></div>
    <div class="scent-tab">Lavender</div>
    <p class="origin">Handcrafted in Bellhaven</p>
  </section>
</main>
</body>
</html>
```